Ferncliff Nutrients

Hi WP designers, this is my first time trying Pixel Guild ;-)

I would like a responsive woocommerce/wordpress theme for a company called Ferncliff nutrients. You can get an idea of what we sell, and how bad our old site is here:http://www.ferncliffnutrients-example.com.sg/

Would love to see any type of modern looking design, a few guidelines:
- We've got a logo (see attached)
- We like green as a base for the colour scheme to match the logo but open to ideas

Target Market(s)

90% of customers will be Singaporean looking for good deals on top brands they already buy.

Industry/Entity Type

It Company

Font styles to use
Other font styles liked:
• Open Sans

Colors
9bcb3c
add136
cadf82
0492cd
eb1f27
a6459a
f78f20
ffc214

Requirements
Must have
• Sign In/Sign UpNewsletter sign up: best dealsFeatured deals sectionRatings/Reviews on products
Nice to have
• We're open to any ideas but would perhaps like to see something minimalist and easy on the eyes.
• Try to keep mostly images and white space
Should not have
• Too much text

```html
<!DOCTYPE html>
<html lang="en">
<head>
<meta charset="utf-8">
<title>Ferncliff Nutrients</title>
<link href="https://fonts.googleapis.com/css2?family=Open+Sans:ital,wght@0,400;0,600;0,700;0,800;1,400&display=swap" rel="stylesheet">
<style>
:root{
  --green:#add136;
  --green-dark:#8cbd1c;
  --green-btn:#9bcb3c;
  --blue:#0492cd;
  --red:#eb1f27;
  --price:#b0000f;
  --purple:#a6459a;
  --orange:#f78f20;
  --gold:#ffc214;
  --ink:#333;
  --muted:#777;
  --panel:#efefef;
  --line:#e3e3e3;
  --footer:#f4f4f4;
  --bar:#2b2b2b;
}
*{box-sizing:border-box;margin:0;padding:0}
html,body{width:1200px;height:2296px;overflow:hidden;background:#fff}
body{position:relative;font-family:'Open Sans',sans-serif;color:var(--ink)}
.abs{position:absolute}
a{color:inherit;text-decoration:none}

/* header */
.brand{left:101px;top:56px;display:flex;align-items:center;gap:14px;white-space:nowrap}
.brand-dot{width:34px;height:34px;border-radius:50%;background:var(--green-dark)}
.brand-name{font-size:33px;font-weight:600;color:#222;letter-spacing:.5px}
.search{left:836px;top:32px;width:168px;height:29px;border:1px solid #ccc;font-size:12px;padding:6px 12px;color:#333;display:flex;justify-content:space-between;align-items:center}
.lang{left:1015px;top:32px;width:84px;height:29px;border:1px solid #ccc;font-size:12px;padding:6px 8px;display:flex;align-items:center;gap:6px}
.flag{width:16px;height:11px;background:linear-gradient(#c33 50%,#fff 50%)}
.cart-total{left:836px;top:89px;font-size:15px;font-weight:700;color:var(--red)}
.cart-icon{left:891px;top:81px;width:34px;height:34px;border-radius:50%;background:var(--red)}
.btn{height:34px;font-size:13px;font-weight:600;color:#fff;display:flex;align-items:center;justify-content:center;border-radius:3px}
.btn-signup{left:952px;top:81px;width:71px;background:var(--blue)}
.btn-signin{left:1032px;top:81px;width:67px;background:var(--purple)}

/* nav */
.nav{left:0;top:150px;width:1200px;height:49px;background:var(--green)}
.nav ul{list-style:none;position:absolute;left:100px;top:0;display:flex;height:49px}
.nav li{font-size:15px;font-weight:600;color:#2a2a2a;display:flex;align-items:center;padding:0 29px;height:49px;white-space:nowrap}
.nav li.active{background:var(--green-dark);padding:0 24px}

/* hero */
.hero{left:0;top:199px;width:1200px;height:413px;background:linear-gradient(90deg,#3f2a1b,#5a3a22 40%,#4a2f1c)}
.hero-sub{left:605px;top:300px;font-size:31px;font-weight:700;color:#fff;white-space:nowrap}
.hero-title{left:605px;top:340px;font-size:42px;font-weight:800;color:#fff;white-space:nowrap}
.hero-btn{left:605px;top:401px;width:101px;height:37px;background:var(--orange);border-radius:3px;color:#222;font-size:15px;font-weight:600;display:flex;align-items:center;justify-content:center}
.dots{left:551px;top:573px;width:100px;height:20px;border-radius:10px;background:#222;display:flex;align-items:center;justify-content:center;gap:10px}
.dots i{width:9px;height:9px;border-radius:50%;background:#fff}
.dots i:first-child{background:none;border:1px solid #fff}

/* welcome */
.welcome-title{left:0;top:654px;width:1200px;text-align:center;font-size:23px;color:var(--orange)}
.welcome-text{left:124px;top:692px;width:952px;text-align:center;font-size:14.5px;line-height:22px;color:var(--muted)}
.promo{left:114px;top:796px;width:973px;height:104px;background:var(--panel);border:1px solid #e4e4e4}
.promo p{position:absolute;left:30px;top:32px;width:620px;font-size:14px;line-height:22px;color:#666}
.promo-brand{position:absolute;left:688px;top:36px;font-size:22px;font-weight:700;color:#1a6f8a;white-space:nowrap}
.promo-partner{position:absolute;left:874px;top:26px;display:flex;align-items:center;gap:6px;white-space:nowrap}
.promo-partner span.c{width:48px;height:48px;border-radius:50%;border:2px solid #2d8a3e}
.promo-partner span.t{font-size:13px;color:#2d8a3e;font-weight:600}

/* deals */
.section-title{font-size:23px;font-weight:400;color:var(--purple)}
.cards{display:flex;gap:27px}
.card{width:222px;border:1px solid var(--line);text-align:center;position:relative}
.card .img{margin:6px;height:141px;background:linear-gradient(#f0f0f0,#e6e6e6)}
.card h3{font-size:15px;font-weight:400;color:var(--blue);line-height:20px;margin-top:14px}
.price{margin-top:12px;font-size:15px}
.price s{color:#e05a5a;margin-right:12px}
.price b{color:var(--price);font-weight:600}
.stars{margin-top:6px;font-size:22px;letter-spacing:1px;color:var(--gold);line-height:22px}
.reviews{font-size:12.5px;color:var(--muted)}
.featured .card{height:250px}
.best .card{height:293px}
.rule{height:1px;background:var(--line)}

/* sidebar */
.side-title{font-size:23px;color:var(--blue)}
.newsletter{left:860px;top:981px;width:230px;height:167px;background:var(--panel)}
.field{position:absolute;left:11px;width:208px;height:40px;background:#fff;font-size:12.5px;color:#999;padding:11px 12px}
.submit{position:absolute;left:136px;top:116px;width:83px;height:36px;background:var(--green-btn);color:#222;font-size:14px;font-weight:600;display:flex;align-items:center;justify-content:center}
.categories{left:860px;top:1200px;width:230px;height:481px;background:var(--panel);padding:12px 0 0 18px}
.categories li{list-style:none;font-size:13.5px;color:#555;line-height:29.2px}
.categories li::before{content:"•";color:#999;margin-right:8px}

/* testimonial */
.testi-title{left:0;top:1722px;width:1200px;text-align:center;font-size:22px;color:var(--red)}
.avatar{left:132px;top:1764px;width:116px;height:116px;border-radius:50%;background:linear-gradient(#e8e0d8,#cdbfb2);border:5px solid #fff;box-shadow:0 2px 6px rgba(0,0,0,.25)}
.quote{left:272px;top:1770px;width:812px;font-size:14.5px;line-height:23px;font-style:italic;color:#777}
.quote-name{left:272px;top:1852px;font-size:15px;color:var(--price)}
.arrow{top:1808px}

/* footer */
.footer{left:0;top:1937px;width:1200px;height:249px;background:var(--footer)}
.f-head{font-size:17px;color:#333}
.f-text{font-size:12.5px;line-height:19.5px;color:#888}
.vline{width:1px;background:#ddd;top:1957px;height:210px}
.contact p{font-size:13px;color:#333;line-height:19px;margin-bottom:10px;font-weight:600;white-space:nowrap}
.contact p.mail{color:var(--blue);font-weight:400;font-size:12px;letter-spacing:-.2px}
.card-tag{top:1998px;height:28px;border:1px solid #ccc;background:#fff;font-size:9px;font-weight:600;color:#333;display:flex;align-items:center;justify-content:center;white-space:nowrap}
.badge{left:893px;top:1968px;width:84px;height:84px;border-radius:50%;background:var(--gold)}
.brands-strip{left:649px;top:2090px;width:447px;height:44px;background:#c9c9c9;display:flex;align-items:center;justify-content:space-around;font-size:18px;font-weight:700;color:#555;white-space:nowrap}
.bar{left:0;top:2186px;width:1200px;height:110px;background:var(--bar)}
.bar-links{position:absolute;left:101px;top:28px;font-size:12.5px;color:#ccc;word-spacing:2px}
.copy{position:absolute;left:101px;top:64px;font-size:12.5px;color:#ccc}
.social{position:absolute;left:908px;top:49px;display:flex;gap:16px}
.social i{width:22px;height:22px;border-radius:50%;background:#777}
</style>
</head>
<body>

<header>
  <div class="abs brand"><span class="brand-dot"></span><span class="brand-name">FERNCLIFF NUTRIENTS</span></div>
  <div class="abs search">Search
    <svg width="14" height="14" viewBox="0 0 14 14"><circle cx="5.5" cy="5.5" r="4" fill="none" stroke="#222" stroke-width="2"/><line x1="8.5" y1="8.5" x2="13" y2="13" stroke="#222" stroke-width="2.5"/></svg>
  </div>
  <div class="abs lang"><span class="flag"></span>Eng
    <svg width="8" height="5" viewBox="0 0 8 5" style="margin-left:auto"><path d="M0 0h8L4 5z" fill="#333"/></svg>
  </div>
  <div class="abs cart-total">$0.00</div>
  <div class="abs cart-icon">
    <svg width="34" height="34" viewBox="0 0 34 34"><path d="M10 14h14l-2 9h-10z" fill="#fff"/><path d="M13 14l4-5 4 5" fill="none" stroke="#fff" stroke-width="1.8"/></svg>
  </div>
  <a class="abs btn btn-signup">SIGNUP</a>
  <a class="abs btn btn-signin">SIGNIN</a>
</header>

<nav class="abs nav">
  <ul>
    <li class="active">HOME</li><li>SPECIAL OFFERS</li><li>BOOKMARK</li><li>ACCOUNT</li><li>BASKET</li><li>CHECKOUT</li><li>SUPPORT</li><li>SEARCH</li>
  </ul>
</nav>

<section>
  <div class="abs hero" role="img" aria-label="Wooden spoon of supplement capsules with green leaves on a dark wooden table"></div>
  <div class="abs hero-sub">Suspendisse tempor purus</div>
  <div class="abs hero-title">NUNC VOLUTPAT</div>
  <a class="abs hero-btn">Read more</a>
  <div class="abs dots"><i></i><i></i><i></i><i></i></div>
</section>

<section>
  <h1 class="abs welcome-title" style="font-weight:400">Welcome to Ferncliff Nutrients</h1>
  <p class="abs welcome-text">Ferncliff Nutrients is founded through a collaboration between partners from Sunny Singapore and Down Under.&nbsp; We are an ONLINE ONLY Shop, which allows us to offer cheap prices as we have low overheads. We hope to take the hassle out of your vitamin and health supplement shopping by providing them to you at wholesale prices shipped direct from Australia to the comfort of your home.</p>
  <div class="abs promo">
    <p>We aim to be your supplier of choice by providing you with the best possible deal for quality products such as Halvenmoor, Brisquel and Merrowind Labs internationally.</p>
    <span class="promo-brand">HALVENMOOR</span>
    <div class="promo-partner"><span class="c"></span><span class="t">Brisquel</span></div>
  </div>
</section>

<section class="featured">
  <h2 class="abs section-title" style="left:107px;top:936px">Featured Deals</h2>
  <div class="abs cards" style="left:109px;top:981px">
    <div class="card"><div class="img" role="img" aria-label="Supplement bottle with red label"></div><h3>Halvenmoor CoQ10 150mg<br>Caps 30</h3><div class="price"><s>$62.00</s><b>$38.50</b></div></div>
    <div class="card"><div class="img" role="img" aria-label="White supplement tub with red label"></div><h3>Halvenmoor CoQ10 150mg<br>Caps 30</h3><div class="price"><s>$62.00</s><b>$38.50</b></div></div>
    <div class="card"><div class="img" role="img" aria-label="Supplement bottle with teal label"></div><h3>Halvenmoor CoQ10 150mg<br>Caps 30</h3><div class="price"><s>$62.00</s><b>$38.50</b></div></div>
  </div>
  <div class="abs rule" style="left:107px;top:1268px;width:732px"></div>
</section>

<section class="best">
  <h2 class="abs section-title" style="left:107px;top:1302px">Best Deals</h2>
  <div class="abs cards" style="left:109px;top:1347px">
    <div class="card"><div class="img" role="img" aria-label="Supplement bottle with blue label"></div><h3>Halvenmoor CoQ10 150mg<br>Caps 30</h3><div class="price"><s>$62.00</s><b>$38.50</b></div><div class="stars">★★★★☆</div><div class="reviews">(26 reviews)</div></div>
    <div class="card"><div class="img" role="img" aria-label="Supplement bottle with orange label"></div><h3>Halvenmoor CoQ10 150mg<br>Caps 30</h3><div class="price"><s>$62.00</s><b>$38.50</b></div><div class="stars">★★★★☆</div><div class="reviews">(26 reviews)</div></div>
    <div class="card"><div class="img" role="img" aria-label="Yellow supplement box"></div><h3>Halvenmoor CoQ10 150mg<br>Caps 30</h3><div class="price"><s>$62.00</s><b>$38.50</b></div><div class="stars">★★★★☆</div><div class="reviews">(26 reviews)</div></div>
  </div>
  <div class="abs rule" style="left:107px;top:1676px;width:732px"></div>
</section>

<aside>
  <h2 class="abs side-title" style="left:861px;top:936px;font-weight:400">Newsletter Signup</h2>
  <form class="abs newsletter">
    <div class="field" style="top:12px">Name</div>
    <div class="field" style="top:63px">E-mail</div>
    <div class="submit">SUBMIT</div>
  </form>
  <h2 class="abs side-title" style="left:861px;top:1163px;font-weight:400">Categories</h2>
  <ul class="abs categories">
    <li>Antioxidants</li><li>Brain Health</li><li>Cardiovascular</li><li>Digestive Health</li><li>Energy Support</li><li>Essential Fatty Acids</li><li>Immune Health</li><li>Joint Health</li><li>Kids</li><li>Men</li><li>Minerals</li><li>Natural</li><li>Reproductive Health</li><li>Sleep</li><li>Vitamins</li><li>Women</li>
  </ul>
</aside>

<section>
  <h2 class="abs testi-title" style="font-weight:400">Client’s Testimonials</h2>
  <svg class="abs arrow" style="left:40px" width="20" height="30" viewBox="0 0 20 30"><path d="M16 2L4 15l12 13" fill="none" stroke="#bbb" stroke-width="2.5"/></svg>
  <svg class="abs arrow" style="left:1140px" width="20" height="30" viewBox="0 0 20 30"><path d="M4 2l12 13L4 28" fill="none" stroke="#bbb" stroke-width="2.5"/></svg>
  <div class="abs avatar" role="img" aria-label="Customer portrait"></div>
  <p class="abs quote">“&nbsp; Nam a malesuada libero. Duis sodales et libero vel interdum. Interdum et malesuada fames ac ante ipsum primis in faucibus. Donec lobortis dui tortor, eu lobortis felis mattis nec. Sed justo quam, luctus eu mauris eget, euismod dapibus sem. Sed tempus feugiat ante, at ornare libero volutpat sed. Maecenas quis magna magna.&nbsp; ”</p>
  <div class="abs quote-name">Tobin Garrow - NY</div>
</section>

<footer>
  <div class="abs footer"></div>
  <h3 class="abs f-head" style="left:101px;top:1962px;font-weight:400">About Us</h3>
  <p class="abs f-text" style="left:101px;top:2000px;width:236px">Donec eget molestie odio. Ut quis lacus egestas, dapibus sem vitae, tincidunt nulla. Cras dignissim bibendum accumsan. Maecenas tristique felis id arcu adipiscing, ut viverra enim facilisis. Nam non tortor pulvinar.</p>
  <a class="abs" style="left:101px;top:2131px;font-size:12.5px;color:var(--blue)">Know more</a>
  <div class="abs vline" style="left:349px"></div>
  <h3 class="abs f-head" style="left:372px;top:1962px;font-weight:400">Contact us</h3>
  <div class="abs contact" style="left:372px;top:2002px;width:245px">
    <p>SGP: +65 3100 2040<br>(Mon-Fri 9-5pm)</p>
    <p>AUS: +61 8 6100 3050</p>
    <p>Fax : +65 3100 2040</p>
    <p class="mail">E-Mail :info@ferncliffnutrients-example.com</p>
  </div>
  <div class="abs vline" style="left:622px"></div>
  <div class="abs card-tag" style="left:648px;width:44px">Quenpay</div>
  <div class="abs card-tag" style="left:700px;width:42px">Tovix</div>
  <div class="abs card-tag" style="left:750px;width:50px">Norra Flex</div>
  <div class="abs card-tag" style="left:809px;width:44px">Norra</div>
  <div class="abs badge"></div>
  <h3 class="abs f-head" style="left:648px;top:2056px;font-weight:400">Brands</h3>
  <div class="abs brands-strip"><span>HALVENMOOR</span><span>Brisquel</span><span>Merrowind Labs</span></div>

  <div class="abs bar">
    <div class="bar-links">Home &nbsp;|&nbsp; Special Offers &nbsp;|&nbsp; Bookmark &nbsp;|&nbsp; Account &nbsp;|&nbsp; Basket &nbsp;|&nbsp; Checkout &nbsp;|&nbsp; Support &nbsp;|&nbsp; Search</div>
    <div class="copy">Copyright ©&nbsp; 2014&nbsp; Ferncliff Nutrients.&nbsp;&nbsp; All rights reserved.</div>
    <div class="social"><i></i><i></i><i></i><i></i><i></i></div>
  </div>
</footer>

</body>
</html>
```